Rabbit Meat Label

We need a label for a shrink-wrapped tray of rabbit. The label does not need to be fancy, we just want a simple sticker to show customers a mock-up of what it may look like. The label is approximately 5" x 2.75". The label will go on top of the rabbit, so it will not lay flat. Please take that into consideration

The rabbit specifically is farm raised. Whole cut-up with 2 fore-legs, 2 hind legs and back.

There is nutritional information on the back, so please mention that somewhere on the label.

Industry/Entity Type

Farm

Requirements
Must have
• Please leave spaces for KFPB seals and other misc items. They are about 0.5" squares.
Should not have
• Do not have anything like "Made in the USA" or "All Natural." This will be added later, if need be.

```html
<!DOCTYPE html>
<html lang="en">
<head>
<meta charset="utf-8">
<title>Farm Raised Rabbit Label</title>
<link rel="stylesheet" href="https://fonts.googleapis.com/css2?family=Arimo:wght@400&display=swap">
<style>
  :root {
    --kraft: #c69c6d;
    --maroon: #7d3f3e;
    --ink: #111111;
    --paper: #ffffff;
    --rule: #1a1a1a;
  }
  html, body {
    margin: 0;
    padding: 0;
    overflow: hidden;
    background: var(--kraft);
  }
  .label {
    position: relative;
    width: 1200px;
    height: 2179px;
    background: var(--kraft);
    font-family: "Arimo", Arial, sans-serif;
    overflow: hidden;
  }
  .rabbit-art {
    position: absolute;
    left: 276px;
    top: 73px;
    width: 756px;
    height: 828px;
    border-radius: 40% 45% 35% 40%;
    background: radial-gradient(ellipse at 65% 60%, #7d3f3e 0%, #9a6a55 45%, #c69c6d 75%);
  }
  .cut-heading {
    position: absolute;
    left: 0;
    width: 1200px;
    top: 965px;
    margin: 0;
    text-align: center;
    color: var(--maroon);
    font-size: 118px;
    font-weight: 400;
    line-height: 1;
    letter-spacing: -1px;
  }
  .cut-box {
    position: absolute;
    top: 1139px;
    width: 311px;
    height: 305px;
    border-radius: 36px;
    background: var(--maroon);
    color: var(--paper);
    text-align: center;
  }
  .cut-box--fore { left: 81px; }
  .cut-box--hind { left: 450px; }
  .cut-box--back { left: 825px; }
  .cut-count {
    display: block;
    font-size: 170px;
    line-height: 1;
    margin-top: 20px;
  }
  .cut-name {
    display: block;
    font-size: 58px;
    line-height: 1;
    margin-top: 6px;
  }
  .cut-box--back .cut-name {
    font-size: 100px;
    margin-top: 90px;
  }
  .plus {
    position: absolute;
    top: 1240px;
    width: 60px;
    text-align: center;
    color: var(--paper);
    font-size: 64px;
    line-height: 1;
  }
  .plus--one { left: 391px; }
  .plus--two { left: 764px; }
  .rule {
    position: absolute;
    left: 0;
    width: 1200px;
    height: 9px;
    background: var(--rule);
  }
  .rule--a1 { top: 1498px; }
  .rule--a2 { top: 1519px; }
  .rule--b1 { top: 1774px; }
  .rule--b2 { top: 1797px; }
  .product-origin {
    position: absolute;
    left: 134px;
    top: 1562px;
    color: var(--ink);
    line-height: 0.95;
    font-size: 84px;
  }
  .product-origin span { display: block; }
  .product-origin .origin-raised { font-size: 76px; }
  .product-name {
    position: absolute;
    left: 462px;
    top: 1560px;
    margin: 0;
    color: var(--maroon);
    font-size: 206px;
    font-weight: 400;
    line-height: 1;
    letter-spacing: -2px;
  }
  .back-note {
    position: absolute;
    right: 30px;
    top: 2080px;
    color: var(--ink);
    font-size: 47px;
    line-height: 1;
  }
</style>
</head>
<body>
  <main class="label">
    <div class="rabbit-art" role="img" aria-label="Outline of a sitting rabbit with the foreleg, hind leg and back cuts shaded in maroon"></div>

    <h2 class="cut-heading">Whole cut-up with</h2>

    <div class="cut-box cut-box--fore">
      <span class="cut-count">2</span>
      <span class="cut-name">forelegs</span>
    </div>
    <span class="plus plus--one">+</span>
    <div class="cut-box cut-box--hind">
      <span class="cut-count">2</span>
      <span class="cut-name">hind legs</span>
    </div>
    <span class="plus plus--two">+</span>
    <div class="cut-box cut-box--back">
      <span class="cut-name">back</span>
    </div>

    <div class="rule rule--a1"></div>
    <div class="rule rule--a2"></div>

    <div class="product-origin">
      <span class="origin-farm">Farm</span>
      <span class="origin-raised">Raised</span>
    </div>
    <h1 class="product-name">Rabbit</h1>

    <div class="rule rule--b1"></div>
    <div class="rule rule--b2"></div>

    <p class="back-note">nutritional info on the back</p>
  </main>
</body>
</html>
```